Stonevale Depot needs a Self-Mailer Brochure Design

NOTE: DO NOT COPY OUR CURRENT BROCHURE DESIGN, WE DON'T LIKE IT AND LOOKING FOR SOMETHING NEW.

I am in charge of marketing at Stonevale Depot. I need create a new self-mailer brochure with our products.

Brief introduction:
• We are wholesaler specializing in home hardware and building supplies. We sell high-end products at better prices.
• Here's some of the items we sell: Bathtub Sales, Faucet Sales, Range Hood
Sales, Shower Sales, Sink Sales, Toilet Sales, Tile Sales, Kitchen supply
sales, Bathroom Supply Sales, Vanities, Lighting, Door Hardware, Mouldings etc.
• Areas Served: Greater Phoenix Area. We are trying to target local businesses in the Phoenix area. Our zip code is 85040.

We would like to create a new self-mailer brochure, that is going to
list our products. The current self-mailer brochure we have is not as organized as we need it to be. We need to make it well-organized and more efficient for our potential customers. I'm attaching our current self-mailer brochure as a reference, Please see the current self-mailer brochure to get an idea of what we need exactly, it will help you to come up with a better concept of putting it all together.

• On the first page, we'd like to include all the essential information about us, and our products- our logo and address, the discounts we provide, and the variety of products that we offer.
• On the other pages, we'd like to list our products with images and descriptions, just like in the current brochure.
• Please make it look appealing to the customer, start the listing with vanities/faucets/surfaces etc.
• You could include the "compare prices" section, just like in current brochure, but only on the first page, instead of every item (Our competitor is Harrick, you can find it in the current brochure)
• We're open to suggestions, so please advise on the design (Simple clean lines, high-end, luxury theme would work best)
• Also, it is important to include all the necessary requirements for a self-mailer so we meet the required specification (you can find the requirements online)

Please find all the imagery and descriptions on our website- https://www.stonevaledepot.example/ - all the images in high res.
The format is 8/5X11", 2 pages, on both sides.

Please email me at northgate.mira@mailbox.example, or text me through the platform if you have any questions!
Current brochure and logo are attached,

Looking forward to hear back from you!

Mira

Target Market(s)

Local Businesses in Phoenix

Industry/Entity Type

Building Product

Font styles to use
Serif

Colors
abd036
000000
5c5c5c
ffffff

Requirements
Must have
• We would like to create a new self-mailer brochure, that is going to
• list our products. The current self-mailer brochure we have is not as organized as we need it to be. We need to make it well-organized and more efficient for our potential customers. I'm attaching our current self-mailer brochure as a reference, Please see the current self-mailer brochure to get an idea of what we need exactly, it will help you to come up with a better concept of putting it all together.
• • On the first page, we'd like to include all the essential information about us, and our products- our logo and address, the discounts we provide, and the variety of products that we offer.
• • On the other pages, we'd like to list our products with images and descriptions, just like in the current brochure.
• • Please make it look appealing to the customer, start the listing with vanities/faucets/surfaces etc. by category (check our website to get familiar with categories)
• • You could include the "compare prices" section, just like in current brochure, but only on the first page, instead of every item (Our competitor is Harrick, you can find it in the current brochure)
• • We're open to suggestions, so please advise on the design (Simple clean lines, high-end, luxury theme would work best)
• • Also, it is important to include all the necessary requirements for a self-mailer so we meet the required specification (you can find the requirements online)

```html
<!DOCTYPE html>
<html lang="en">
<head>
<meta charset="utf-8">
<title>Stonevale Depot – Product Spread</title>
<link href="https://fonts.googleapis.com/css2?family=Oswald:wght@400;500&family=Open+Sans:wght@400;600;700&display=swap" rel="stylesheet">
<style>
  :root{
    --lime:#abd036;
    --black:#000000;
    --graphite:#5c5c5c;
    --white:#ffffff;
    --red:#e0301e;
    --page-left:#0c0c0c;
    --page-right:#1b1b1b;
    --backdrop:#d9d9dc;
    --rule:#56661c;
    --caption:#c9c9c9;
  }
  *{box-sizing:border-box}
  html,body{margin:0;width:1200px;height:1200px;overflow:hidden;background:var(--backdrop);font-family:'Open Sans',Arial,sans-serif}
  .spread{position:absolute;left:40px;top:222px;width:1120px;height:756px;display:flex;box-shadow:0 18px 40px rgba(0,0,0,.25)}
  .page{width:560px;height:100%;padding:20px 24px;color:var(--white)}
  .page-left{background:var(--page-left)}
  .page-right{background:var(--page-right)}

  .section-head{display:flex;align-items:center;gap:12px;height:38px;margin:14px 0 10px}
  .page > .section-head:first-child{margin-top:4px}
  .section-head .bar{flex:1;height:14px;background:var(--lime)}
  .section-head .bar-top{align-self:flex-start}
  .section-head .bar-bottom{align-self:flex-end}
  .section-title{font-family:'Oswald','Arial Narrow',sans-serif;font-weight:500;font-size:24px;letter-spacing:.5px;text-transform:uppercase;margin:0;line-height:1;white-space:nowrap}

  .tiles{display:grid;grid-template-columns:repeat(8,1fr);gap:8px 8px;margin:0;padding:0}
  .tiles-9{grid-template-columns:repeat(9,1fr);gap:8px 6px}
  .tiles-3{grid-template-columns:repeat(3,1fr)}
  .tiles-4{grid-template-columns:repeat(4,1fr)}
  .item{position:relative;list-style:none;min-width:0}
  .photo{height:50px;background:linear-gradient(135deg,#f6f6f6 0%,#c4c4c4 100%);border:1px solid var(--white)}
  .photo.warm{background:linear-gradient(135deg,#d8b48c 0%,#7a5336 100%)}
  .photo.dark{background:linear-gradient(135deg,#e9e9e9 0%,#55585c 100%)}
  .tag{position:absolute;top:2px;right:0;background:var(--lime);padding:1px 2px;display:flex;flex-direction:column;align-items:flex-end;line-height:1}
  .tag b{font-size:7px;font-weight:700;color:var(--black)}
  .tag s{font-size:5.5px;font-weight:600;color:var(--red)}
  .item p{margin:2px 0 0;font-size:5.5px;line-height:1.2;color:var(--caption);white-space:nowrap;overflow:hidden;text-overflow:ellipsis}

  .vanity-grid{display:grid;grid-template-columns:1.08fr 1fr;border-top:1px solid var(--rule);border-bottom:1px solid var(--rule)}
  .collection{padding:8px 8px 10px}
  .collection-verano{border-right:1px solid var(--rule);border-bottom:1px solid var(--rule)}
  .collection-calloway{grid-row:span 2}
  .collection-brixton{border-right:1px solid var(--rule)}
  .feature{display:flex;gap:8px;margin-bottom:8px}
  .hero-photo{flex:0 0 132px;height:92px;background:linear-gradient(160deg,#f2f2f2 0%,#9a9a9a 60%,#2c2c2c 100%)}
  .hero-photo.blue{background:linear-gradient(160deg,#5b6f9a 0%,#b9c0cf 55%,#efefef 100%)}
  .details h3{margin:0 0 3px;font-family:'Oswald','Arial Narrow',sans-serif;font-weight:400;font-size:11px;color:var(--lime);text-transform:uppercase;letter-spacing:.5px}
  .details p{margin:0;font-size:6px;line-height:1.45;color:var(--caption)}
  .brixton-row{margin:8px 0 0}
</style>
</head>
<body>
<div class="spread">

  <section class="page page-left">
    <header class="section-head"><span class="bar bar-top"></span><h2 class="section-title">Bathroom</h2><span class="bar bar-bottom"></span></header>
    <ul class="tiles">
      <li class="item"><div class="photo dark" role="img" aria-label="Vessel sink photo"></div><span class="tag"><b>$24.95</b><s>$39.95</s></span><p>Vessel sink</p></li>
      <li class="item"><div class="photo" role="img" aria-label="Towel bar photo"></div><span class="tag"><b>$8.95</b><s>$14.95</s></span><p>Towel bar</p></li>
      <li class="item"><div class="photo" role="img" aria-label="Pop-up drain photo"></div><span class="tag"><b>$6.95</b><s>$11.95</s></span><p>Popup drain</p></li>
      <li class="item"><div class="photo" role="img" aria-label="Robe hook photo"></div><span class="tag"><b>$4.95</b><s>$8.95</s></span><p>Robe hook</p></li>
      <li class="item"><div class="photo" role="img" aria-label="Single lever faucet photo"></div><span class="tag"><b>$34.95</b><s>$59.95</s></span><p>Lever faucet</p></li>
      <li class="item"><div class="photo dark" role="img" aria-label="Waterfall faucet photo"></div><span class="tag"><b>$44.95</b><s>$69.95</s></span><p>Waterfall faucet</p></li>
      <li class="item"><div class="photo" role="img" aria-label="Tissue holder photo"></div><span class="tag"><b>$9.95</b><s>$16.95</s></span><p>Tissue holder</p></li>
      <li class="item"><div class="photo warm" role="img" aria-label="Bathtub photo"></div><span class="tag"><b>$39.95</b><s>$64.95</s></span><p>Tub filler</p></li>
      <li class="item"><div class="photo" role="img" aria-label="Basin faucet photo"></div><span class="tag"><b>$29.95</b><s>$49.95</s></span><p>Basin faucet</p></li>
      <li class="item"><div class="photo" role="img" aria-label="Chrome faucet photo"></div><span class="tag"><b>$37.95</b><s>$58.95</s></span><p>Chrome tap</p></li>
      <li class="item"><div class="photo" role="img" aria-label="Tall faucet photo"></div><span class="tag"><b>$41.95</b><s>$66.95</s></span><p>Tall faucet</p></li>
      <li class="item"><div class="photo" role="img" aria-label="Shower valve photo"></div><span class="tag"><b>$29.95</b><s>$45.95</s></span><p>Shower valve</p></li>
      <li class="item"><div class="photo dark" role="img" aria-label="Square faucet photo"></div><span class="tag"><b>$26.95</b><s>$42.95</s></span><p>Square faucet</p></li>
      <li class="item"><div class="photo" role="img" aria-label="Wall faucet photo"></div><span class="tag"><b>$32.95</b><s>$52.95</s></span><p>Wall faucet</p></li>
      <li class="item"><div class="photo warm" role="img" aria-label="Freestanding tub photo"></div><span class="tag"><b>$399</b><s>$649</s></span><p>Freestanding tub</p></li>
      <li class="item"><div class="photo" role="img" aria-label="Oval sink photo"></div><span class="tag"><b>$19.95</b><s>$34.95</s></span><p>Oval sink</p></li>
      <li class="item"><div class="photo dark" role="img" aria-label="Cascade faucet photo"></div><span class="tag"><b>$37.95</b><s>$59.95</s></span><p>Cascade faucet</p></li>
      <li class="item"><div class="photo" role="img" aria-label="Modern faucet photo"></div><span class="tag"><b>$62.95</b><s>$94.95</s></span><p>Modern faucet</p></li>
      <li class="item"><div class="photo warm" role="img" aria-label="Vessel basin photo"></div><span class="tag"><b>$49.95</b><s>$79.95</s></span><p>Vessel basin</p></li>
      <li class="item"><div class="photo" role="img" aria-label="Shower head photo"></div><span class="tag"><b>$18.95</b><s>$29.95</s></span><p>Shower head</p></li>
      <li class="item"><div class="photo" role="img" aria-label="Towel ring photo"></div><span class="tag"><b>$7.95</b><s>$12.95</s></span><p>Towel ring</p></li>
      <li class="item"><div class="photo dark" role="img" aria-label="Shower column photo"></div><span class="tag"><b>$54.95</b><s>$89.95</s></span><p>Shower column</p></li>
      <li class="item"><div class="photo" role="img" aria-label="Hand shower photo"></div><span class="tag"><b>$14.95</b><s>$24.95</s></span><p>Hand shower</p></li>
      <li class="item"><div class="photo" role="img" aria-label="Round sink photo"></div><span class="tag"><b>$19.95</b><s>$32.95</s></span><p>Round sink</p></li>
      <li class="item"><div class="photo warm" role="img" aria-label="Stone sink photo"></div><span class="tag"><b>$59.95</b><s>$95.95</s></span><p>Stone sink</p></li>
      <li class="item"><div class="photo" role="img" aria-label="Low faucet photo"></div><span class="tag"><b>$22.95</b><s>$36.95</s></span><p>Low faucet</p></li>
      <li class="item"><div class="photo" role="img" aria-label="Rain shower set photo"></div><span class="tag"><b>$74.95</b><s>$119.95</s></span><p>Rain set</p></li>
      <li class="item"><div class="photo dark" role="img" aria-label="Bridge faucet photo"></div><span class="tag"><b>$59.95</b><s>$89.95</s></span><p>Bridge faucet</p></li>
      <li class="item"><div class="photo warm" role="img" aria-label="Widespread faucet photo"></div><span class="tag"><b>$55.95</b><s>$88.95</s></span><p>Widespread faucet</p></li>
      <li class="item"><div class="photo" role="img" aria-label="Mixer tap photo"></div><span class="tag"><b>$39.95</b><s>$62.95</s></span><p>Mixer tap</p></li>
      <li class="item"><div class="photo" role="img" aria-label="Tub spout photo"></div><span class="tag"><b>$12.95</b><s>$21.95</s></span><p>Tub spout</p></li>
      <li class="item"><div class="photo dark" role="img" aria-label="Drain cover photo"></div><span class="tag"><b>$9.95</b><s>$15.95</s></span><p>Drain cover</p></li>
    </ul>

    <header class="section-head"><span class="bar bar-top"></span><h2 class="section-title">Kitchen</h2><span class="bar bar-bottom"></span></header>
    <ul class="tiles">
      <li class="item"><div class="photo" role="img" aria-label="Single bowl sink photo"></div><span class="tag"><b>$64.95</b><s>$99.95</s></span><p>Single bowl</p></li>
      <li class="item"><div class="photo" role="img" aria-label="Double bowl sink photo"></div><span class="tag"><b>$84.95</b><s>$129.95</s></span><p>Double bowl</p></li>
      <li class="item"><div class="photo dark" role="img" aria-label="Undermount sink photo"></div><span class="tag"><b>$144.95</b><s>$219.95</s></span><p>Undermount sink</p></li>
      <li class="item"><div class="photo" role="img" aria-label="Divided sink photo"></div><span class="tag"><b>$94.95</b><s>$149.95</s></span><p>Divided sink</p></li>
      <li class="item"><div class="photo" role="img" aria-label="Bar sink photo"></div><span class="tag"><b>$179.95</b><s>$259.95</s></span><p>Bar sink</p></li>
      <li class="item"><div class="photo dark" role="img" aria-label="Farmhouse sink photo"></div><span class="tag"><b>$249.95</b><s>$379.95</s></span><p>Farmhouse sink</p></li>
      <li class="item"><div class="photo" role="img" aria-label="Offset sink photo"></div><span class="tag"><b>$169.95</b><s>$249.95</s></span><p>Offset sink</p></li>
      <li class="item"><div class="photo" role="img" aria-label="Prep sink photo"></div><span class="tag"><b>$179.95</b><s>$269.95</s></span><p>Prep sink</p></li>
      <li class="item"><div class="photo warm" role="img" aria-label="Pull-down faucet photo"></div><span class="tag"><b>$74.95</b><s>$119.95</s></span><p>Pulldown faucet</p></li>
      <li class="item"><div class="photo warm" role="img" aria-label="Spring faucet photo"></div><span class="tag"><b>$54.95</b><s>$89.95</s></span><p>Spring faucet</p></li>
      <li class="item"><div class="photo warm" role="img" aria-label="Arc faucet photo"></div><span class="tag"><b>$79.95</b><s>$124.95</s></span><p>Arc faucet</p></li>
      <li class="item"><div class="photo" role="img" aria-label="Pot filler photo"></div><span class="tag"><b>$89.95</b><s>$139.95</s></span><p>Pot filler</p></li>
      <li class="item"><div class="photo" role="img" aria-label="Soap dispenser photo"></div><span class="tag"><b>$12.95</b><s>$19.95</s></span><p>Soap dispenser</p></li>
      <li class="item"><div class="photo dark" role="img" aria-label="Sink grid photo"></div><span class="tag"><b>$24.95</b><s>$39.95</s></span><p>Sink grid</p></li>
      <li class="item"><div class="photo" role="img" aria-label="Strainer photo"></div><span class="tag"><b>$8.95</b><s>$14.95</s></span><p>Basket strainer</p></li>
      <li class="item"><div class="photo" role="img" aria-label="Air gap photo"></div><span class="tag"><b>$6.95</b><s>$10.95</s></span><p>Air gap</p></li>
    </ul>

    <header class="section-head"><span class="bar bar-top"></span><h2 class="section-title">Moulding</h2><span class="bar bar-bottom"></span></header>
    <ul class="tiles">
      <li class="item"><div class="photo" role="img" aria-label="Crown moulding profile"></div><span class="tag"><b>$9.82</b><s>$14.90</s></span><p>Crown moulding</p></li>
      <li class="item"><div class="photo" role="img" aria-label="Base moulding profile"></div><span class="tag"><b>$7.95</b><s>$12.40</s></span><p>Base moulding</p></li>
      <li class="item"><div class="photo" role="img" aria-label="Casing profile"></div><span class="tag"><b>$8.32</b><s>$12.90</s></span><p>Door casing</p></li>
      <li class="item"><div class="photo" role="img" aria-label="Chair rail profile"></div><span class="tag"><b>$6.46</b><s>$9.80</s></span><p>Chair rail</p></li>
      <li class="item"><div class="photo" role="img" aria-label="Shoe moulding profile"></div><span class="tag"><b>$5.42</b><s>$8.30</s></span><p>Shoe moulding</p></li>
      <li class="item"><div class="photo" role="img" aria-label="Cove moulding profile"></div><span class="tag"><b>$6.05</b><s>$9.20</s></span><p>Cove moulding</p></li>
      <li class="item"><div class="photo" role="img" aria-label="Quarter round profile"></div><span class="tag"><b>$4.31</b><s>$6.90</s></span><p>Quarter round</p></li>
      <li class="item"><div class="photo" role="img" aria-label="Window stool profile"></div><span class="tag"><b>$14.98</b><s>$22.40</s></span><p>Window stool</p></li>
    </ul>
  </section>

  <section class="page page-right">
    <header class="section-head"><span class="bar bar-top"></span><h2 class="section-title">Vanities</h2><span class="bar bar-bottom"></span></header>
    <div class="vanity-grid">
      <article class="collection collection-verano">
        <div class="feature">
          <div class="hero-photo" role="img" aria-label="Verano double vanity with mirror"></div>
          <div class="details">
            <h3>Verano</h3>
            <p>Available sizes: 36" 48" 60" 72"<br>FEATURES:<br>• Solid wood construction<br>• Brushed nickel hardware<br>• Soft close drawers<br>INCLUDES:<br>• Matching framed mirror<br>• Marble top, porcelain sinks</p>
          </div>
        </div>
        <ul class="tiles tiles-4">
          <li class="item"><div class="photo dark" role="img" aria-label="Verano 72 inch vanity"></div><span class="tag"><b>$995</b><s>$1,490</s></span><p>Verano 72"</p></li>
          <li class="item"><div class="photo dark" role="img" aria-label="Verano 36 inch vanity"></div><span class="tag"><b>$560</b><s>$840</s></span><p>Verano 36"</p></li>
          <li class="item"><div class="photo dark" role="img" aria-label="Verano 60 inch vanity"></div><span class="tag"><b>$875</b><s>$1,310</s></span><p>Verano 60"</p></li>
          <li class="item"><div class="photo dark" role="img" aria-label="Verano 48 inch vanity"></div><span class="tag"><b>$745</b><s>$1,120</s></span><p>Verano 48"</p></li>
        </ul>
      </article>

      <article class="collection collection-calloway">
        <div class="feature">
          <div class="hero-photo blue" role="img" aria-label="Calloway white double vanity"></div>
          <div class="details">
            <h3>Calloway</h3>
            <p>Available sizes: 48" 60" 72" White<br>FEATURES:<br>• Solid wood construction<br>• Brushed nickel hardware<br>• Soft close drawers<br>INCLUDES:<br>• Matching framed mirror<br>• Marble top, porcelain sinks</p>
          </div>
        </div>
        <ul class="tiles tiles-3">
          <li class="item"><div class="photo dark" role="img" aria-label="Calloway grey vanity"></div><span class="tag"><b>$940</b><s>$1,410</s></span><p>Calloway grey</p></li>
          <li class="item"><div class="photo dark" role="img" aria-label="Calloway espresso vanity"></div><span class="tag"><b>$1,089</b><s>$1,630</s></span><p>Calloway espresso</p></li>
          <li class="item"><div class="photo dark" role="img" aria-label="Calloway dark vanity"></div><span class="tag"><b>$1,089</b><s>$1,630</s></span><p>Calloway dark</p></li>
          <li class="item"><div class="photo" role="img" aria-label="Calloway white vanity"></div><span class="tag"><b>$795</b><s>$1,190</s></span><p>Calloway white</p></li>
          <li class="item"><div class="photo" role="img" aria-label="Calloway single vanity"></div><span class="tag"><b>$945</b><s>$1,420</s></span><p>Calloway single</p></li>
          <li class="item"><div class="photo" role="img" aria-label="Calloway double vanity"></div><span class="tag"><b>$945</b><s>$1,420</s></span><p>Calloway double</p></li>
          <li class="item"><div class="photo" role="img" aria-label="Calloway 60 inch vanity"></div><span class="tag"><b>$940</b><s>$1,410</s></span><p>Calloway 60"</p></li>
          <li class="item"><div class="photo dark" role="img" aria-label="Calloway 48 inch vanity"></div><span class="tag"><b>$745</b><s>$1,120</s></span><p>Calloway 48"</p></li>
          <li class="item"><div class="photo dark" role="img" aria-label="Calloway 72 inch vanity"></div><span class="tag"><b>$1,025</b><s>$1,540</s></span><p>Calloway 72"</p></li>
        </ul>
      </article>

      <article class="collection collection-brixton">
        <div class="feature">
          <div class="hero-photo" role="img" aria-label="Brixton grey double vanity"></div>
          <div class="details">
            <h3>Brixton</h3>
            <p>Available sizes: 24" 36" 48" 60"<br>FEATURES:<br>• Solid wood construction<br>• Brushed nickel hardware<br>• Soft close drawers<br>INCLUDES:<br>• Matching framed mirror<br>• Marble top, porcelain sinks</p>
          </div>
        </div>
      </article>
    </div>

    <ul class="tiles tiles-9 brixton-row">
      <li class="item"><div class="photo dark" role="img" aria-label="Brixton 24 inch vanity"></div><span class="tag"><b>$389</b><s>$580</s></span><p>Brixton 24"</p></li>
      <li class="item"><div class="photo" role="img" aria-label="Brixton 36 inch vanity"></div><span class="tag"><b>$545</b><s>$820</s></span><p>Brixton 36"</p></li>
      <li class="item"><div class="photo" role="img" aria-label="Brixton 60 inch vanity"></div><span class="tag"><b>$1,025</b><s>$1,540</s></span><p>Brixton 60"</p></li>
      <li class="item"><div class="photo" role="img" aria-label="Brixton 48 inch vanity"></div><span class="tag"><b>$895</b><s>$1,340</s></span><p>Brixton 48"</p></li>
      <li class="item"><div class="photo" role="img" aria-label="Brixton white vanity"></div><span class="tag"><b>$775</b><s>$1,160</s></span><p>Brixton white</p></li>
      <li class="item"><div class="photo dark" role="img" aria-label="Brixton grey vanity"></div><span class="tag"><b>$425</b><s>$640</s></span><p>Brixton grey</p></li>
      <li class="item"><div class="photo" role="img" aria-label="Brixton single vanity"></div><span class="tag"><b>$545</b><s>$820</s></span><p>Brixton single</p></li>
      <li class="item"><div class="photo dark" role="img" aria-label="Brixton espresso vanity"></div><span class="tag"><b>$575</b><s>$860</s></span><p>Brixton espresso</p></li>
      <li class="item"><div class="photo dark" role="img" aria-label="Brixton 30 inch vanity"></div><span class="tag"><b>$745</b><s>$1,120</s></span><p>Brixton 30"</p></li>
    </ul>

    <header class="section-head"><span class="bar bar-top"></span><h2 class="section-title">Door Hardware</h2><span class="bar bar-bottom"></span></header>
    <ul class="tiles">
      <li class="item"><div class="photo warm" role="img" aria-label="Bronze lever set"></div><span class="tag"><b>$15.95</b><s>$24.95</s></span><p>Bronze lever</p></li>
      <li class="item"><div class="photo warm" role="img" aria-label="Passage lever set"></div><span class="tag"><b>$15.95</b><s>$24.95</s></span><p>Passage lever</p></li>
      <li class="item"><div class="photo" role="img" aria-label="Privacy lever set"></div><span class="tag"><b>$15.95</b><s>$24.95</s></span><p>Privacy lever</p></li>
      <li class="item"><div class="photo" role="img" aria-label="Dummy lever set"></div><span class="tag"><b>$15.95</b><s>$24.95</s></span><p>Dummy lever</p></li>
      <li class="item"><div class="photo dark" role="img" aria-label="Single deadbolt"></div><span class="tag"><b>$5.95</b><s>$9.95</s></span><p>Single deadbolt</p></li>
      <li class="item"><div class="photo" role="img" aria-label="Passage knob"></div><span class="tag"><b>$6.95</b><s>$10.95</s></span><p>Passage knob</p></li>
      <li class="item"><div class="photo" role="img" aria-label="Privacy knob"></div><span class="tag"><b>$5.95</b><s>$9.95</s></span><p>Privacy knob</p></li>
      <li class="item"><div class="photo" role="img" aria-label="Entry lever set"></div><span class="tag"><b>$15.95</b><s>$24.95</s></span><p>Entry lever</p></li>
      <li class="item"><div class="photo" role="img" aria-label="Entry knob"></div><span class="tag"><b>$5.95</b><s>$9.95</s></span><p>Entry knob</p></li>
      <li class="item"><div class="photo warm" role="img" aria-label="Keyed lever set"></div><span class="tag"><b>$15.95</b><s>$24.95</s></span><p>Keyed lever</p></li>
      <li class="item"><div class="photo warm" role="img" aria-label="Brass deadbolt"></div><span class="tag"><b>$9.95</b><s>$15.95</s></span><p>Brass deadbolt</p></li>
    </ul>
  </section>

</div>
</body>
</html>
```